rt for guide - bartholomew finch personal speaking/consulting website

custom website for my personal speaking/consulting services brand, you can see the basic site we are using as a placeholder at www.rtforguide.example now. I want to re-position this to more of a personal brand site and have video samples of speaking events, downloadable content, a video blog, and links to podcast. I really like the design of dorianwelk.example and the feature set should be fairly similar to his. I'll begin to compile more stock images etc. to use for sliders like he has done, for now we'll need to use stock imagery or existing photography from my social accounts. You can get a feel for social at all platforms/bfinchbroker i.e. facebook.com/bfinchbroker. the site should be primarily geared toward showcasing speaking/consulting services and content, as well as be flexible to allow for additional downloadables etc. in the future.

Target Market(s)

entrepreneurs and leaders looking to grow themselves, their business, and those they lead.

Coding

Coded - Design and coding required

Number of Pages Required

3 page

Font styles to use
Sans Serif

Colors

Designer to choose colors to be used in the design.

Requirements
Must have
• modern slick design, video blog, podcast feed, registration for people to subscribe to newsletter

```html
<!DOCTYPE html>
<html lang="en">
<head>
<meta charset="utf-8">
<title>RT for Guide — Bartholomew Finch</title>
<link href="https://fonts.googleapis.com/css2?family=Mulish:wght@400;600;700;800;900&display=swap" rel="stylesheet">
<style>
:root{
  --teal:#4aa3b5;
  --cyan:#17b3d9;
  --cyan-light:#6fe0f2;
  --yellow:#f4d21c;
  --navy:#17203a;
  --footer:#1e2637;
  --ink:#222a33;
  --white:#ffffff;
  --mist:#e4e8ee;
  --mist-band:#dfe4ea;
}
*{box-sizing:border-box;margin:0;padding:0}
html,body{width:1200px;height:5341px;overflow:hidden}
body{font-family:"Mulish",Arial,sans-serif;color:var(--ink);background:var(--white);position:relative}
.abs{position:absolute}
.photo{position:absolute;display:block}
.heading{font-family:"Mulish",Arial,sans-serif}

/* hero */
.hero{position:absolute;left:0;top:0;width:1200px;height:677px;overflow:hidden}
.hero .photo{inset:0;background:
  radial-gradient(ellipse 220px 260px at 250px 300px,rgba(232,226,220,.55),transparent 70%),
  radial-gradient(ellipse 240px 280px at 640px 280px,rgba(235,232,228,.5),transparent 70%),
  radial-gradient(ellipse 220px 260px at 900px 360px,rgba(240,238,234,.5),transparent 70%),
  linear-gradient(90deg,#3b4a6a 0%,#5a4c46 30%,#4a4038 55%,#6a6258 80%,#3c4252 100%)}
.hero-shade{position:absolute;inset:0;background:linear-gradient(180deg,rgba(10,14,24,.3),rgba(10,14,24,.1) 50%,rgba(10,14,24,.45))}
.badge{left:222px;top:26px;width:136px;height:44px;border-radius:8px;background:#111;border:2px solid #aaa}
.nav{right:112px;top:36px;display:flex;gap:34px;align-items:center;font-size:12px;font-weight:700;color:var(--white);text-transform:uppercase;letter-spacing:.5px}
.nav .nav-cta{background:var(--cyan);padding:7px 16px;border-radius:2px}
.brand-title{font-weight:900;color:var(--white);line-height:1;text-align:center}
.hero-title{left:0;width:1200px;top:262px;font-size:92px}
.brand-title .line-two{display:block;padding-left:90px}
.hero-tag{left:0;width:1200px;top:458px;text-align:center;font-weight:800;font-size:23px;line-height:1.35;color:var(--white)}
.hero-tag .hl-cyan{color:var(--cyan-light)}
.hero-tag .hl-yellow{color:var(--yellow)}
.btn{display:flex;align-items:center;justify-content:center;font-weight:800;text-transform:uppercase;letter-spacing:.6px}
.hero-btn{left:454px;top:531px;width:292px;height:46px;background:var(--cyan-light);color:var(--navy);font-size:15px}

/* become leaders */
.leaders{position:absolute;left:0;top:677px;width:1200px;height:676px;background:var(--teal)}
.leaders-frame{left:110px;top:89px;width:745px;height:491px;border:2px solid rgba(255,255,255,.85)}
.leaders-kicker{left:224px;top:158px;font-size:44px;font-weight:800;color:var(--white)}
.leaders-title{left:218px;top:200px;font-size:118px;font-weight:800;color:var(--white);line-height:1;letter-spacing:-1px}
.leaders-copy{left:224px;top:362px;width:470px;font-size:15px;line-height:1.5;color:var(--white)}
.leaders-copy b{color:var(--yellow)}
.read-more{left:224px;top:484px;width:200px;height:44px;border:2px solid var(--white);color:var(--white);font-size:14px;justify-content:space-between;padding:0 0 0 16px;text-transform:none;font-weight:700}
.read-more span.arrow{width:44px;height:40px;display:flex;align-items:center;justify-content:center;background:var(--cyan)}

/* inspiring */
.inspiring{position:absolute;left:0;top:1353px;width:1200px;height:430px}
.inspiring .photo{left:224px;top:93px;width:421px;height:256px;background:
  radial-gradient(ellipse 120px 80px at 300px 200px,rgba(200,210,220,.45),transparent 70%),
  linear-gradient(135deg,#24303f,#5b6c7d 50%,#2f3a48)}
.photo-tag{font-size:12px;font-weight:800;color:var(--white);border:1px solid var(--white);padding:6px 12px;background:rgba(0,0,0,.3);letter-spacing:1px}
.inspiring .photo-tag{left:336px;top:212px}
.inspiring-title{left:570px;top:136px;font-size:88px;font-weight:800;color:var(--cyan);line-height:1}
.inspiring-copy{left:673px;top:248px;width:290px;font-size:12px;line-height:1.5;color:#333}

/* videos */
.section-title{width:1200px;left:0;text-align:center;font-weight:800;color:var(--cyan)}
.videos-title{top:1804px;font-size:44px}
.video{position:absolute;background:#222}
.video-main{left:224px;top:1891px;width:752px;height:374px;background:
  radial-gradient(ellipse 180px 90px at 300px 250px,rgba(190,150,120,.5),transparent 70%),
  radial-gradient(circle at 45% 45%,#4a3e36,#161618 70%)}
.video-a{left:224px;top:2286px;width:367px;height:242px;background:
  radial-gradient(ellipse 140px 90px at 150px 120px,rgba(245,243,238,.8),transparent 70%),
  linear-gradient(135deg,#d9d5cf,#8b8d8e 60%,#4b4f55)}
.video-b{left:609px;top:2286px;width:367px;height:242px;background:
  radial-gradient(ellipse 140px 70px at 180px 140px,rgba(200,180,160,.55),transparent 70%),
  linear-gradient(135deg,#4a3f39,#8e7f76 50%,#3a3632)}
.play{position:absolute;left:50%;top:50%;transform:translate(-50%,-50%)}
.video-label{position:absolute;right:24px;bottom:18px;font-size:15px;font-weight:800;color:var(--white);letter-spacing:.5px}

/* products */
.products{position:absolute;left:0;top:2621px;width:1200px;height:600px}
.products-band{left:224px;top:292px;width:976px;height:221px;background:var(--mist-band)}
.products-panel{left:719px;top:0;width:481px;height:292px;background:var(--mist)}
.products .photo-main{left:224px;top:0;width:495px;height:292px;background:
  radial-gradient(ellipse 160px 90px at 250px 180px,rgba(210,210,210,.45),transparent 70%),
  linear-gradient(120deg,#2f2f2f,#7d7d7d 50%,#262626)}
.products-title{left:730px;top:230px;font-size:52px;font-weight:800;color:var(--cyan);line-height:1}
.products .photo-one{left:352px;top:345px;width:285px;height:168px;background:linear-gradient(135deg,#5b4b3f,#ab9580 55%,#3e352e)}
.products .photo-two{left:659px;top:345px;width:288px;height:168px;background:linear-gradient(135deg,#4e4239,#988172 55%,#342d28)}
.products .photo-tag{font-size:11px;padding:5px 10px}
.cam{position:absolute;left:14px;bottom:12px;width:18px;height:13px;border:2px solid var(--white)}
.socials-row{left:862px;top:540px;display:flex;gap:5px}
.socials-row span{width:17px;height:17px;border-radius:50%;background:var(--ink)}

/* featured podcasts */
.featured-title{top:3248px;font-size:50px}
.podcasts{position:absolute;left:0;top:3401px;width:1200px;height:545px}
.pod{position:absolute}
.pod-1{left:0;top:0;width:271px;height:500px;background:
  radial-gradient(ellipse 90px 160px at 150px 260px,rgba(220,170,130,.55),transparent 70%),
  linear-gradient(160deg,#2e2019,#8a5f40 50%,#241a14)}
.pod-2{left:271px;top:72px;width:341px;height:473px;background:
  radial-gradient(ellipse 110px 200px at 170px 260px,rgba(70,55,50,.55),transparent 70%),
  linear-gradient(180deg,#f2f2f2,#d8d8d8)}
.pod-3{left:612px;top:0;width:271px;height:545px;background:
  radial-gradient(ellipse 90px 170px at 135px 300px,rgba(240,170,160,.7),transparent 70%),
  linear-gradient(180deg,#9c7b62,#cfa294 50%,#6d5f53)}
.pod-4{left:883px;top:72px;width:317px;height:473px;background:
  radial-gradient(ellipse 90px 120px at 170px 300px,rgba(60,60,60,.45),transparent 70%),
  linear-gradient(180deg,#cfe0e6,#8fa7ae 60%,#6a7a80)}
.watch{position:absolute;width:196px;height:50px;background:var(--white);border:2px solid var(--cyan);display:flex;align-items:center;justify-content:space-between;padding-left:28px;font-size:15px;font-weight:700;color:var(--cyan)}
.watch .arrow{width:50px;height:46px;display:flex;align-items:center;justify-content:center;border-left:2px solid var(--cyan)}
.watch.dark{background:var(--navy);color:var(--white)}

/* cta */
.cta{position:absolute;left:0;top:3946px;width:1200px;height:605px;background:
  radial-gradient(ellipse 200px 260px at 850px 300px,rgba(60,70,95,.7),transparent 70%),
  radial-gradient(ellipse at 40% 30%,#2b3550,#141b2e 70%)}
.cta-title{position:absolute;left:0;width:1200px;top:4178px;font-size:88px}
.cta-btn{left:460px;top:4408px;width:280px;height:46px;border:2px solid var(--white);color:var(--white);font-size:15px;position:absolute}

/* contact */
.contact-title{top:4630px;font-size:44px}
.field{position:absolute;border:2px solid var(--cyan-light);font-size:11px;color:#555;padding:8px 10px;background:var(--white)}
.field-name{left:310px;top:4718px;width:274px;height:32px}
.field-email{left:605px;top:4718px;width:278px;height:32px}
.field-msg{left:310px;top:4772px;width:573px;height:82px}
.submit{position:absolute;left:456px;top:4879px;width:274px;height:34px;background:var(--cyan-light);color:var(--white);font-size:15px;letter-spacing:10px}

/* footer */
.footer{position:absolute;left:0;top:4985px;width:1200px;height:356px;background:var(--footer);color:#cfd4dc}
.footer-socials{position:absolute;left:501px;top:72px;display:flex;gap:14px}
.footer-socials span{width:30px;height:30px;border-radius:50%;background:#8a919d}
.footer-info{position:absolute;top:146px;font-size:12px;color:#cfd4dc}
.footer-rule{position:absolute;left:224px;top:214px;width:752px;height:1px;background:#4a5264}
.footer-copy{position:absolute;left:0;width:1200px;top:230px;text-align:center;font-size:11px;line-height:1.6;color:#aeb5c0}
</style>
</head>
<body>

<header class="hero">
  <div class="photo" role="img" aria-label="Three smiling men sitting together in front of a graffiti wall"></div>
  <div class="hero-shade"></div>
  <div class="abs badge" aria-label="Podcast listing badge"></div>
  <nav class="abs nav"><span>Resources</span><span>Blog</span><span>Contact</span><span class="nav-cta">Subscribe Us</span></nav>
  <h1 class="abs brand-title hero-title">RT for<span class="line-two">Guide</span></h1>
  <p class="abs hero-tag">The Place where <span class="hl-cyan">ENTREPRENEURS</span><br>Come to Become <span class="hl-yellow">LEADERS</span></p>
  <a class="abs btn hero-btn">Subscribe to our podcast</a>
</header>

<section class="leaders">
  <div class="abs leaders-frame"></div>
  <h2 class="abs heading leaders-kicker">Become</h2>
  <h2 class="abs heading leaders-title">Leaders</h2>
  <p class="abs leaders-copy"><b>BARTHOLOMEW FINCH</b> and <b>MARCUS OYELARAN</b> reveal secrets on how to polish your leadership skills, shift your business mindset, and empower your team. Subscribe to this blog to get the latest tips and tricks to help you be a successful entrepreneur.</p>
  <a class="abs btn read-more">Read more <span class="arrow"><svg width="12" height="14" viewBox="0 0 12 14"><path d="M1 1l10 6-10 6z" fill="#fff"/></svg></span></a>
  <div class="photo" style="left:730px;top:167px;width:246px;height:331px;background:radial-gradient(ellipse 70px 90px at 123px 130px,rgba(225,180,160,.6),transparent 70%),linear-gradient(180deg,#2f4f86,#5f7fa8 60%,#1f2c4a)" role="img" aria-label="Portrait of a man in a suit and red tie"></div>
  <div class="photo" style="left:983px;top:167px;width:217px;height:331px;background:radial-gradient(ellipse 65px 85px at 108px 130px,rgba(215,175,150,.55),transparent 70%),linear-gradient(180deg,#2e5d84,#8a7c6e 55%,#3a3a3a)" role="img" aria-label="Portrait of a bearded man in glasses"></div>
</section>

<section class="inspiring">
  <div class="photo" role="img" aria-label="Team working at laptops around a table"></div>
  <span class="abs photo-tag">PODCASTS</span>
  <h2 class="abs heading inspiring-title">Inspiring</h2>
  <p class="abs inspiring-copy">BARTHOLOMEW FINCH and MARCUS OYELARAN share secrets on how to polish your leadership skills, shift your business mindset, and empower your team. Subscribe to this blog to get the latest tips and tricks to help you be a successful entrepreneur.</p>
</section>

<h2 class="abs heading section-title videos-title">Subscribe Our Products</h2>
<div class="video video-main" role="img" aria-label="Hand tossing a pair of dice in dark light">
  <svg class="play" width="56" height="56" viewBox="0 0 56 56"><circle cx="28" cy="28" r="26" fill="none" stroke="#fff" stroke-width="2"/><path d="M22 17l17 11-17 11z" fill="#fff"/></svg>
  <span class="video-label">WATCH FULL VIDEO</span>
</div>
<div class="video video-a" role="img" aria-label="People planning with papers on a desk">
  <svg class="play" width="60" height="60" viewBox="0 0 60 60"><circle cx="30" cy="30" r="29" fill="#fff"/><path d="M24 18l18 12-18 12z" fill="#222"/></svg>
  <span class="video-label">WATCH FULL VIDEO</span>
</div>
<div class="video video-b" role="img" aria-label="Team meeting around a wooden table">
  <span class="video-label">WATCH FULL VIDEO</span>
</div>

<section class="products">
  <div class="abs products-band"></div>
  <div class="abs products-panel"></div>
  <div class="photo photo-main" role="img" aria-label="Team collaborating in a black and white office">
    <span class="abs photo-tag" style="left:190px;top:130px">TEAM BUILDING</span>
    <span class="cam"></span>
  </div>
  <h2 class="abs heading products-title">Products</h2>
  <div class="photo photo-one" role="img" aria-label="Group of entrepreneurs talking at a table">
    <span class="abs photo-tag" style="left:86px;top:72px">ENTREPRENEURS</span>
    <span class="cam"></span>
  </div>
  <div class="photo photo-two" role="img" aria-label="Colleagues discussing leadership at a desk">
    <span class="abs photo-tag" style="left:70px;top:72px">LEADERSHIP SKILLS</span>
    <span class="cam"></span>
  </div>
  <div class="abs socials-row"><span></span><span></span><span></span><span></span><span></span><span></span></div>
</section>

<h2 class="abs heading section-title featured-title">FEATURED PODCASTS</h2>
<section class="podcasts">
  <div class="pod pod-1" role="img" aria-label="Young woman in glasses in a warm lit cafe"></div>
  <div class="pod pod-2" role="img" aria-label="Man in a white t-shirt against a pale wall"></div>
  <div class="pod pod-3" role="img" aria-label="Smiling woman in sunglasses and a pink top"></div>
  <div class="pod pod-4" role="img" aria-label="Man sitting on a seaside pier"></div>
  <a class="watch" style="left:339px;top:0">Watch Now <span class="arrow"><svg width="12" height="14" viewBox="0 0 12 14"><path d="M1 1l10 6-10 6z" fill="#17203a"/></svg></span></a>
  <a class="watch" style="left:943px;top:0">Watch Now <span class="arrow"><svg width="12" height="14" viewBox="0 0 12 14"><path d="M1 1l10 6-10 6z" fill="#17203a"/></svg></span></a>
  <a class="watch dark" style="left:32px;top:495px">Watch Now <span class="arrow"><svg width="12" height="14" viewBox="0 0 12 14"><path d="M1 1l10 6-10 6z" fill="#fff"/></svg></span></a>
  <a class="watch dark" style="left:648px;top:495px">Watch Now <span class="arrow"><svg width="12" height="14" viewBox="0 0 12 14"><path d="M1 1l10 6-10 6z" fill="#fff"/></svg></span></a>
</section>

<section class="cta" role="img" aria-label="Speaker addressing a large audience in a dark hall"></section>
<h2 class="brand-title cta-title">RT for<span class="line-two">Guide</span></h2>
<a class="btn cta-btn">Subscribe to our podcast</a>

<h2 class="abs heading section-title contact-title">Make following your Aim</h2>
<div class="field field-name">Name</div>
<div class="field field-email">Email</div>
<div class="field field-msg">Message</div>
<a class="btn submit">Submit</a>

<footer class="footer">
  <div class="footer-socials"><span></span><span></span><span></span><span></span><span></span><span></span></div>
  <p class="footer-info" style="left:224px">Address : 12 Harbour Lane, Suite 4, Springfield</p>
  <p class="footer-info" style="left:590px">Email : hello@rtforguide.example</p>
  <p class="footer-info" style="left:850px">Phone : +00 0000 0000</p>
  <div class="footer-rule"></div>
  <p class="footer-copy">©2024 RT for Guide<br>Proudly Brought To You By Northwind Studio<br>Website Disclosure</p>
</footer>

</body>
</html>
```